Verpackung für Hanf-Nudeln gesucht
Zielgruppe
Wir haben Hanf & Natur Shops und Onlineshop. Zielgruppe sind Menschen die gesund und bewusst Leben möchten.
Aufgabenstellung
Verpackung für Hanf-Nudeln (Suppen-, Band-, Spaghetti-, Hörnchennudeln). 500g abgepackt.
Wichtig: handgemacht in Österreich, 100 % vegan und bio
sie enthalten Dinkel- und Hanfmehl sowie geringe Mengen an Selvin KRISTALLSALZ und werden mit nitratfreiem Wasser erzeugt. Die Hanfnudeln sind vollkommen frei von synthetischen Hilfsmitteln. Kochzeit ca. 3 Minuten., Info für alle Allergiker, Hanfnudeln sind NICHT GLUTENFREI., Zutaten: Dinkel, Hanfmehl, Steinsalz, nitratfreies Wasser
Verpackungsvorschläge bitte
Modernes Design, passend zu unseren anderen Tirovelmo Produkten

```html
<!DOCTYPE html>
<html lang="de">
<head>
<meta charset="UTF-8">
<title>Tirovelmo Hanfnudeln – Hörnchennudeln</title>
<link href="https://fonts.googleapis.com/css2?family=Montserrat:wght@300;400;600;700;900&display=swap" rel="stylesheet">
<style>
  :root {
    --backdrop: #ececec;
    --kraft: #c9a57b;
    --kraft-dark: #b9946a;
    --kraft-light: #d6b88f;
    --ink: #2b2926;
    --label: #e6e6e6;
    --brand-green: #4f8a4a;
    --pasta-deep: #e9b84a;
    --pasta-light: #f6dc93;
    --white: #ffffff;
  }
  * { margin: 0; padding: 0; box-sizing: border-box; }
  html, body { width: 1200px; height: 1200px; overflow: hidden; }
  body {
    background: var(--backdrop);
    font-family: "Montserrat", sans-serif;
    color: var(--ink);
    position: relative;
  }
  .bag {
    position: absolute;
    left: 336px; top: 40px;
    width: 528px; height: 1120px;
    background: var(--kraft);
  }
  .bag__fold {
    position: absolute; left: 0; right: 0; top: 85px;
    height: 2px; background: var(--kraft-dark);
  }
  .bag__artwork {
    position: absolute; left: 0; top: 125px;
    width: 246px; height: 720px;
    background: linear-gradient(160deg, rgba(255,255,255,0.22), rgba(255,255,255,0.06));
  }
  .brand-label {
    position: absolute; left: 192px; top: 0;
    width: 140px; height: 226px;
    background: var(--label);
    display: flex; flex-direction: column; align-items: center; justify-content: flex-end;
    padding-bottom: 24px;
  }
  .brand-label__dot {
    width: 46px; height: 46px; border-radius: 50%;
    background: var(--brand-green);
    margin-bottom: 26px;
  }
  .brand-label__name {
    font-weight: 700; font-size: 13px; letter-spacing: 0.5px;
    color: var(--ink);
  }
  .title {
    position: absolute; left: 93px; top: 285px;
    font-weight: 900; font-size: 116px; line-height: 101px;
    letter-spacing: -2px; color: var(--ink);
  }
  .title span { display: block; }
  .variety {
    position: absolute; left: 206px; top: 522px;
    font-weight: 300; font-size: 34px; line-height: 36px;
    letter-spacing: 1px; color: var(--ink);
  }
  .cook-badge {
    position: absolute; left: 352px; top: 329px;
    width: 148px; height: 148px; border-radius: 50%;
    background: var(--ink); color: var(--white);
    display: flex; flex-direction: column; align-items: center; justify-content: center;
    text-align: center;
  }
  .cook-badge svg { margin-bottom: 10px; }
  .cook-badge__label { font-weight: 300; font-size: 14px; line-height: 18px; }
  .cook-badge__time { font-weight: 700; font-size: 14px; line-height: 18px; }
  .window {
    position: absolute; left: 79px; top: 611px;
    width: 366px; height: 290px;
    background: linear-gradient(180deg, var(--pasta-deep) 0%, var(--pasta-light) 60%, #f3dfa6 100%);
  }
  .claims {
    position: absolute; left: 87px; top: 929px;
    width: 346px; height: 135px;
    border: 2px dotted var(--ink);
    display: grid; grid-template-columns: 131px 1fr; grid-template-rows: 1fr 1fr;
  }
  .claims__handmade {
    grid-row: 1 / 3;
    border-right: 2px dotted var(--ink);
    display: flex; flex-direction: column; align-items: center; justify-content: center;
    font-size: 11px; line-height: 14px; text-align: center;
  }
  .claims__hands-icon {
    width: 80px; height: 60px; margin-bottom: 10px;
    background: rgba(43,41,38,0.12);
  }
  .claims__item {
    display: flex; align-items: center; gap: 26px; padding-left: 48px;
    font-size: 11px;
  }
  .claims__item--vegan { border-bottom: 2px dotted var(--ink); }
</style>
</head>
<body>
  <main class="bag">
    <div class="bag__fold"></div>
    <div class="bag__artwork" role="img" aria-label="Weiße Strichzeichnung von Nudeln"></div>

    <div class="brand-label">
      <div class="brand-label__dot"></div>
      <div class="brand-label__name">TIROVELMO</div>
    </div>

    <h1 class="title"><span>PA</span><span>ST</span><span>A</span></h1>
    <p class="variety">HÖRNCHEN-<br>NUDELN</p>

    <div class="cook-badge">
      <svg width="56" height="50" viewBox="0 0 56 50" fill="none" stroke="#fff" stroke-width="2.5" stroke-linecap="round">
        <path d="M22 2c-3 3 3 5 0 9M30 2c-3 3 3 5 0 9"/>
        <path d="M10 20h36v20a6 6 0 0 1-6 6H16a6 6 0 0 1-6-6z"/>
        <path d="M10 24H4M46 24h6M8 20h40"/>
      </svg>
      <span class="cook-badge__label">KOCHZEIT</span>
      <span class="cook-badge__time">ca. 3 MIN</span>
    </div>

    <div class="window" role="img" aria-label="Sichtfenster mit Hanf-Spiralnudeln"></div>

    <section class="claims">
      <div class="claims__handmade">
        <div class="claims__hands-icon" role="img" aria-label="Symbol zweier Hände"></div>
        <span>handgemacht<br>in Österreich</span>
      </div>
      <div class="claims__item claims__item--vegan">
        <svg width="30" height="26" viewBox="0 0 30 26" fill="none" stroke="#2b2926" stroke-width="2">
          <path d="M2 2l13 22L28 2M8 2l7 13 7-13"/>
        </svg>
        <span>100 % vegan</span>
      </div>
      <div class="claims__item">
        <svg width="30" height="30" viewBox="0 0 30 30" fill="none" stroke="#2b2926" stroke-width="2">
          <path d="M6 26C2 16 10 4 26 4c0 16-10 24-20 22z"/>
          <path d="M6 26C10 18 16 12 22 9"/>
        </svg>
        <span>100 % bio</span>
      </div>
    </section>
  </main>
</body>
</html>
```